UNABLE TO FIND SUITABLE ICT TALENT IN NEW ZEALAND? WE CAN HELP.

We need a brochure to sell our migration services to ICT (Information and Communication Technologies) recruiters in New Zealand. We are a New Zealand based migration company headed by a Licensed Immigration Adviser and we can bring in specific talents into New Zealand. We are aware ICT is in the long term skill shortage area and that recruiters and companies are struggling to find the right ICT talent. So over the past two years we have developed a high quality global ICT talent pool who are keen to work in New Zealand. And we have the expertise to and process their legal entry into New Zealand bring them in at short notice. We need a brochure that conveys a strong New Zealand connect, confidence and trust.

Target Market(s)

New Zealand ICT Recruiters and Companies who need ICT talent

Industry/Entity Type

Communication

Contact Information for Business Card

Corwin Haltey
Senior Manager - Operations
Mobile: 0274318296

Font styles to use
Serif

Requirements
Must have
• A strong ICT and New Zealand theme. Must have the following Maori proverb on the rear with the English translation. The rear side of the card which has this proverb must also have a strong Maori theme.
• Naku te rourou nau te rourou ka ora ai te iwi - With your basket and my basket the people will live
Nice to have
• The brochure/flyer is intended to be an A4 size folded in half, so that we can print and mail it to our target clients. Remember this is an A4 flyer folded in the middle. So it has got cover + back + 2 inside pages in all.

```html
<!DOCTYPE html>
<html lang="en">
<head>
<meta charset="utf-8">
<title>KVR Migration – Brochure Spread</title>
<link href="https://fonts.googleapis.com/css2?family=Josefin+Sans:wght@400;600;700&display=swap" rel="stylesheet">
<style>
  :root{
    --bg:#d9d9d9;
    --purple:#5e5a96;
    --purple-deep:#4f4b86;
    --lavender:#8a86bd;
    --pink:#d98a9a;
    --ink:#1f1f24;
    --white:#ffffff;
    --text-soft:#e6e4f2;
    --silver-1:#f7f7f7;
    --silver-2:#c9c9cc;
  }
  *{box-sizing:border-box;margin:0;padding:0}
  html,body{width:1200px;height:1200px;overflow:hidden;background:var(--bg)}
  body{font-family:"Josefin Sans",sans-serif;position:relative}
  .spread{position:absolute;left:100px;top:246px;width:1000px;height:707px;display:flex;box-shadow:0 18px 40px rgba(0,0,0,.22)}
  .page{position:relative;width:500px;height:707px;overflow:hidden}
  .page svg.page-art{position:absolute;inset:0;width:100%;height:100%}

  /* back page */
  .col{position:absolute;color:var(--text-soft);font-size:8.6px;line-height:1.38}
  .col h2{font-size:12.5px;font-weight:700;color:var(--white);letter-spacing:.6px;text-transform:uppercase;line-height:1.15;padding-bottom:4px;border-bottom:1px solid var(--text-soft);margin-bottom:6px}
  .col p{margin-bottom:10px}
  .col b{color:var(--white);font-weight:700}
  .team{left:34px;top:110px;width:226px}
  .benefits{left:272px;top:56px;width:196px}
  .benefits ul{list-style:none;margin-bottom:26px}
  .benefits li{position:relative;padding-left:10px;margin-bottom:1px}
  .benefits li::before{content:"";position:absolute;left:0;top:4px;width:3px;height:3px;border-radius:50%;background:var(--text-soft)}
  .brand{position:absolute;display:flex;align-items:center;gap:7px;font-family:"Josefin Sans",sans-serif;font-weight:400;color:var(--ink);letter-spacing:1px}
  .brand .dot{border-radius:50%;background:var(--ink)}
  .back-brand{left:40px;top:632px;font-size:15px}
  .back-brand .dot{width:26px;height:26px}
  .divider{position:absolute;left:215px;top:594px;width:1px;height:78px;background:#777}
  .contact{position:absolute;left:232px;top:598px;list-style:none;font-size:10.5px;color:#333;line-height:1.3}
  .contact li{display:flex;gap:7px;margin-bottom:5px;align-items:flex-start}
  .contact svg{width:9px;height:9px;margin-top:2px;flex:none}

  /* front page */
  .front-brand{left:180px;top:46px;font-size:14px}
  .front-brand .dot{width:24px;height:24px}
  .proverb{position:absolute;left:0;right:0;top:498px;text-align:center;color:var(--white)}
  .proverb h1{font-size:19px;font-weight:600;letter-spacing:.5px;margin-bottom:6px}
  .proverb p{font-size:10.5px;font-weight:700;line-height:1.35}
  .web{position:absolute;left:0;right:0;top:600px;display:flex;justify-content:center;align-items:center;gap:8px;color:var(--white);font-size:11px;font-weight:700;letter-spacing:.5px}
  .web svg{width:10px;height:10px}
</style>
</head>
<body>
<main class="spread">

  <!-- Back page -->
  <section class="page page-back">
    <svg class="page-art" viewBox="0 0 500 707" aria-hidden="true">
      <defs>
        <linearGradient id="silver" x1="0" y1="0" x2="1" y2="1">
          <stop offset="0" stop-color="var(--silver-2)"/>
          <stop offset=".45" stop-color="var(--silver-1)"/>
          <stop offset="1" stop-color="var(--silver-2)"/>
        </linearGradient>
      </defs>
      <rect width="500" height="707" fill="url(#silver)"/>
      <path d="M0,0H500V560Q250,610 0,470Z" fill="var(--purple)"/>
      <path d="M0,470Q250,610 500,560" fill="none" stroke="var(--lavender)" stroke-width="10"/>
      <path d="M0,478Q250,620 500,568" fill="none" stroke="var(--pink)" stroke-width="2.5"/>
    </svg>

    <div class="col team">
      <h2>The Team</h2>
      <p><b>Devan Morris</b> is the managing director and a Licensed Immigration Adviser (License No 201904372). A veteran of the migration industry, he is highly acknowledged within the migration industry and was accorded the privilege of a private audience with the Governor General of New Zealand in recognition of his services.</p>
      <p><b>Sunil Varma</b> is a director and brings with him over two decades of ICT experience. He has worked in leading ICT roles in New Zealand for over a decade now and with his technical background he is responsible for candidate assessment to ensure suitability to the New Zealand ICT work environment.</p>
      <p><b>Corwin Haltey</b> is the Senior Operations Manager and your primary contact for engagement and delivery of our services. He has vast experience in New Zealand and Asia and has an enviable track record in education and public relations.</p>
      <p><b>Rohan Pereira</b> is the manager responsible for creation of a high quality ICT talent pool to be attracted and moved to New Zealand. He ensures that only the crème de la crème enter the ICT talent pool available for New Zealand.</p>
    </div>

    <div class="col benefits">
      <h2>Summary of<br>benefits to you</h2>
      <ul>
        <li>Access to a vast high quality and vetted global ICT talent pool.</li>
        <li>A New Zealand based team to co-ordinate all recruitment activities.</li>
        <li>A team that extends your recruitment activities far beyond New Zealand's borders.</li>
        <li>A Licensed Immigration Adviser to process work visas on time.</li>
        <li>No upfront or hidden costs and a commitment to play by the rulebook always.</li>
      </ul>
      <h2>Sounds good.<br>What next?</h2>
      <p>Let's keep it simple and exchange an email agreement to collaborate. You can then start sending us your requirements with absolutely no obligations attached. We will swing into action and start presenting the appropriate CVs to you, coordinate interviews for those shortlisted, process visas upon an offer being made and do whatever else is need.</p>
    </div>

    <div class="brand back-brand"><span class="dot"></span>KVR MIGRATION</div>
    <div class="divider"></div>
    <ul class="contact">
      <li><svg viewBox="0 0 10 10"><path d="M5 0.5A3.3 3.3 0 0 0 1.7 3.8C1.7 6.3 5 9.5 5 9.5S8.3 6.3 8.3 3.8A3.3 3.3 0 0 0 5 0.5Z" fill="#333"/><circle cx="5" cy="3.8" r="1.2" fill="#eee"/></svg><span>KVR Migration Ltd, 48 Kowhai Lane,<br>Riverlea, Hamilton 3216</span></li>
      <li><svg viewBox="0 0 10 10"><rect x="0.5" y="2" width="9" height="6.5" rx="1" fill="#333"/><path d="M1 2.7 5 5.8 9 2.7" fill="none" stroke="#eee" stroke-width=".9"/></svg><span>info@kvr.kiwi</span></li>
      <li><svg viewBox="0 0 10 10"><circle cx="5" cy="5" r="4.3" fill="none" stroke="#333"/><path d="M0.8 5H9.2M5 0.7C2.6 3 2.6 7 5 9.3M5 0.7C7.4 3 7.4 7 5 9.3" fill="none" stroke="#333" stroke-width=".8"/></svg><span>www.kvr.kiwi</span></li>
    </ul>
  </section>

  <!-- Front cover -->
  <section class="page page-front">
    <svg class="page-art" viewBox="0 0 500 707">
      <defs>
        <linearGradient id="coverSky" x1="0" y1="0" x2="0" y2="1">
          <stop offset="0" stop-color="#eeedf5"/>
          <stop offset="1" stop-color="#dcdbe9"/>
        </linearGradient>
        <linearGradient id="photoTone" x1="0" y1="0" x2="1" y2="1">
          <stop offset="0" stop-color="#e8e8ee"/>
          <stop offset=".5" stop-color="#8f8a90"/>
          <stop offset="1" stop-color="#3a3a48"/>
        </linearGradient>
      </defs>
      <rect width="500" height="707" fill="url(#coverSky)" aria-hidden="true"/>
      <rect x="0" y="190" width="500" height="300" fill="url(#photoTone)" role="img" aria-label="Photograph: a candidate in a job interview facing a panel of four business people at a white table"/>
      <path d="M0,0H500V190H0Z" fill="url(#coverSky)" aria-hidden="true"/>
      <g aria-hidden="true">
        <path d="M0,460Q300,470 500,300V707H0Z" fill="var(--purple)"/>
        <path d="M0,460Q300,470 500,300" fill="none" stroke="var(--lavender)" stroke-width="12"/>
        <path d="M0,452Q300,462 500,292" fill="none" stroke="var(--pink)" stroke-width="3"/>
        <path d="M0,448Q300,457 500,287" fill="none" stroke="var(--ink)" stroke-width="2.5"/>
      </g>
    </svg>

    <div class="brand front-brand"><span class="dot"></span>KVR MIGRATION</div>

    <div class="proverb">
      <h1>Naku te rourou nau te rourou ka ora ai te iwi</h1>
      <p>With your basket and my basket the people will live.<br>Let us cooperate and combine our resources to get ahead together.</p>
    </div>
    <div class="web">
      <svg viewBox="0 0 10 10"><circle cx="5" cy="5" r="4.3" fill="none" stroke="#fff"/><path d="M0.8 5H9.2M5 0.7C2.6 3 2.6 7 5 9.3M5 0.7C7.4 3 7.4 7 5 9.3" fill="none" stroke="#fff" stroke-width=".8"/></svg>
      <span>www.kvr.kiwi</span>
    </div>
  </section>

</main>
</body>
</html>
```